Corvane Bookkeeping Services business cards

looking for a double sided business card design. My logo is attached. I am looking for a design similar to the attached. Keen to see what my logo in white on the blue background would look like.

```html
<!DOCTYPE html>
<html lang="en">
<head>
<meta charset="utf-8">
<title>Corvane Bookkeeping Services — Business Cards</title>
<link rel="stylesheet" href="https://fonts.googleapis.com/css2?family=Poppins:wght@400;500;700;800&display=swap">
<style>
  :root {
    --backdrop: #c9c9c9;
    --lime: #9dbb2d;
    --navy: #163f7c;
    --navy-light: #1d4d93;
    --navy-dark: #10305f;
    --ink: #3a3a3a;
    --paper: #ffffff;
  }
  * { box-sizing: border-box; margin: 0; padding: 0; }
  html, body { width: 1200px; height: 900px; overflow: hidden; }
  body {
    background: var(--backdrop);
    font-family: "Poppins", sans-serif;
    position: relative;
  }
  .card {
    position: absolute;
    width: 630px;
    height: 360px;
    border-radius: 26px;
    overflow: hidden;
    box-shadow: 0 10px 24px rgba(0,0,0,.22);
  }
  .card--back { left: 285px; top: 70px; background: var(--navy); }
  .card--front { left: 285px; top: 470px; background: var(--paper); }

  .back-pattern {
    position: absolute; inset: 0;
    background: linear-gradient(135deg, var(--navy-light), var(--navy) 55%, var(--navy-dark));
  }
  .back-brand {
    position: absolute;
    right: 56px; top: 138px;
    display: flex; align-items: center; gap: 14px;
    color: var(--paper);
    font-weight: 700;
    font-size: 26px;
    line-height: 1.15;
  }
  .brand-square {
    width: 30px; height: 30px;
    background: currentColor;
    flex: none;
  }

  .front-brand {
    position: absolute;
    left: 48px; top: 46px;
    display: flex; align-items: center; gap: 16px;
    color: var(--navy);
    font-weight: 700;
    font-size: 28px;
    line-height: 1.15;
  }
  .front-brand .brand-square { width: 38px; height: 38px; }

  .person { position: absolute; left: 60px; top: 166px; }
  .person__name { font-size: 30px; font-weight: 800; color: var(--lime); line-height: 1.1; }
  .person__name span { color: var(--navy); }
  .person__role { font-size: 17px; color: var(--ink); margin-top: 2px; }

  .contacts { position: absolute; left: 60px; top: 260px; list-style: none; }
  .contacts li {
    display: flex; align-items: center; gap: 10px;
    font-size: 16px; color: var(--ink); line-height: 26px;
  }
  .contacts svg { width: 15px; height: 15px; fill: var(--navy); flex: none; }
  .contacts .accent { color: var(--lime); }

  .address {
    position: absolute; right: 44px; top: 198px;
    text-align: right;
    font-size: 16px; color: var(--ink); line-height: 1.35;
  }
</style>
</head>
<body>

  <section class="card card--back">
    <div class="back-pattern" role="img" aria-label="Repeating embossed brand pattern in tones of deep blue"></div>
    <div class="back-brand">
      <span class="brand-square"></span>
      <span>Corvane<br>Bookkeeping Services</span>
    </div>
  </section>

  <section class="card card--front">
    <div class="front-brand">
      <span class="brand-square"></span>
      <span>Corvane<br>Bookkeeping Services</span>
    </div>

    <div class="person">
      <p class="person__name">Elliot <span>Harrow</span></p>
      <p class="person__role">Managing Director</p>
    </div>

    <ul class="contacts">
      <li>
        <svg viewBox="0 0 16 16" aria-hidden="true"><path d="M3.6 1.2l2.3 2.6-1.3 1.8c.9 2.1 2.7 3.9 4.8 4.8l1.8-1.3 2.6 2.3-1.4 2.4C6.6 13.6 2.4 9.4 1.2 3.6z"/></svg>
        044-555 018 274
      </li>
      <li>
        <svg viewBox="0 0 16 16" aria-hidden="true"><path d="M1 3h14v10H1z M1.8 3.6L8 8.6l6.2-5" fill="none" stroke="#163f7c" stroke-width="1.6"/></svg>
        info@corvanebooks.com
      </li>
      <li>
        <svg viewBox="0 0 16 16" aria-hidden="true"><circle cx="8" cy="8" r="6.6" fill="none" stroke="#163f7c" stroke-width="1.4"/><path d="M1.5 8h13M8 1.5c-3 3.5-3 9.5 0 13M8 1.5c3 3.5 3 9.5 0 13" fill="none" stroke="#163f7c" stroke-width="1.2"/></svg>
        <span>www.<span class="accent">corvanebooks</span>.com</span>
      </li>
    </ul>

    <p class="address">87, Linden Quay Road<br>30918, Norland</p>
  </section>

</body>
</html>
```